Quorvane Capital Modern Business Card

We need a modern business card template designed for Quorvane Capital.
Quorvane Capital is a diversified global cryptocurrency investment fund.

The font under the logo: Hiragino Kaku Gothic Pro

Color Hexcode: Main colors white (ffffff) & teal (188383), we are open to adding #fcca46 as an accent

Target Market(s)

Accredited Investors, high net worth individuals and institutional investors

Industry/Entity Type

Investment

Contact Information for Business Card

Contact Information should contain
Name
main phone +1 720 555 0147
cell
email

Font styles to use
Sans Serif
Other font styles liked:
• Hiragino Kaku Gothic Pro

Requirements
Must have
• would like to have icons that identify the contact information
• include our website: www.quorvanecapital.example
• include our Tagline: Diversified Crypto Investment Funds
Nice to have
• Would like to have a simple back side with the logo (without the words) and plenty of space

```html
<!DOCTYPE html>
<html lang="en">
<head>
<meta charset="utf-8">
<title>Quorvane Capital – Business Card</title>
<link rel="stylesheet" href="https://fonts.googleapis.com/css2?family=Montserrat:wght@500;700&family=Noto+Sans+JP:wght@400&family=Roboto+Condensed:wght@700&display=swap">
<style>
  :root {
    --backdrop: #2f4249;
    --teal: #219494;
    --white: #ffffff;
    --ink: #1c1c1c;
    --card-shadow: 0 18px 40px rgba(0, 0, 0, 0.35);
  }
  * { margin: 0; padding: 0; box-sizing: border-box; }
  html, body {
    width: 1200px;
    height: 900px;
    overflow: hidden;
    background: var(--backdrop);
  }
  .canvas {
    position: relative;
    width: 1200px;
    height: 900px;
  }
  .card {
    position: absolute;
    left: 290px;
    width: 620px;
    height: 354px;
    background: var(--white);
    box-shadow: var(--card-shadow);
    overflow: hidden;
  }
  .card--front { top: 58px; }
  .card--back { top: 478px; }

  /* Front */
  .front-panel {
    position: absolute;
    inset: 0;
    background: var(--teal);
    clip-path: polygon(30% 0, 100% 0, 100% 100%, 59% 100%);
  }
  .front-brand {
    position: absolute;
    left: 34px;
    top: 196px;
    display: flex;
    align-items: center;
    gap: 8px;
    font-family: "Noto Sans JP", sans-serif;
    font-weight: 400;
    font-size: 17px;
    letter-spacing: 0.5px;
    color: var(--ink);
  }
  .brand-mark {
    width: 10px;
    height: 10px;
    background: var(--teal);
  }
  .holder {
    position: absolute;
    right: 44px;
    top: 30px;
    text-align: right;
    color: var(--white);
    font-family: "Montserrat", sans-serif;
  }
  .holder-name {
    font-weight: 700;
    font-size: 27px;
    line-height: 1.1;
    letter-spacing: 0.5px;
  }
  .holder-role {
    font-weight: 700;
    font-size: 10px;
    letter-spacing: 0.6px;
  }
  .contact-list {
    position: absolute;
    right: 26px;
    top: 178px;
    list-style: none;
    font-family: "Montserrat", sans-serif;
    font-weight: 500;
    font-size: 11.5px;
    color: var(--white);
    letter-spacing: 0.3px;
  }
  .contact-item {
    display: flex;
    justify-content: flex-end;
    align-items: center;
    gap: 8px;
    height: 17px;
  }
  .contact-icon {
    width: 14px;
    height: 14px;
    flex: none;
  }

  /* Back */
  .back-brand {
    position: absolute;
    left: 0;
    right: 0;
    top: 150px;
    display: flex;
    justify-content: center;
    align-items: center;
    gap: 12px;
    font-family: "Noto Sans JP", sans-serif;
    font-weight: 400;
    font-size: 30px;
    letter-spacing: 0.5px;
    color: var(--ink);
  }
  .back-brand .brand-mark {
    width: 16px;
    height: 16px;
  }
  .tagline {
    position: absolute;
    left: 0;
    right: 0;
    top: 286px;
    text-align: center;
    font-family: "Roboto Condensed", sans-serif;
    font-weight: 700;
    font-size: 17px;
    color: var(--ink);
  }
</style>
</head>
<body>
<main class="canvas">

  <section class="card card--front" aria-label="Business card front">
    <div class="front-panel"></div>

    <div class="front-brand">
      <span class="brand-mark"></span>
      <span>QUORVANE CAPITAL</span>
    </div>

    <div class="holder">
      <p class="holder-name">Elias Marrow</p>
      <p class="holder-role">Energy Advisor</p>
    </div>

    <ul class="contact-list">
      <li class="contact-item">
        <span>+1 720 555 0147</span>
        <svg class="contact-icon" viewBox="0 0 14 14" aria-hidden="true">
          <circle cx="7" cy="7" r="7" fill="#ffffff"/>
          <path d="M3.5 6.5c0-1.6 1.6-2.5 3.5-2.5s3.5.9 3.5 2.5l-1.3.3-.5-1.1H5.3l-.5 1.1z M4.8 7.2h4.4l.6 2.8H4.2z" fill="#219494"/>
        </svg>
      </li>
      <li class="contact-item">
        <span>elias.marrow@quorvanecapital.example</span>
        <svg class="contact-icon" viewBox="0 0 14 14" aria-hidden="true">
          <circle cx="7" cy="7" r="7" fill="#ffffff"/>
          <rect x="3.5" y="4.5" width="7" height="5" fill="#219494"/>
          <path d="M3.5 4.5l3.5 2.8 3.5-2.8" fill="none" stroke="#ffffff" stroke-width="0.8"/>
        </svg>
      </li>
      <li class="contact-item">
        <span>www.quorvanecapital.example</span>
        <svg class="contact-icon" viewBox="0 0 14 14" aria-hidden="true">
          <circle cx="7" cy="7" r="7" fill="#ffffff"/>
          <g fill="none" stroke="#219494" stroke-width="0.9">
            <circle cx="7" cy="7" r="3.6"/>
            <ellipse cx="7" cy="7" rx="1.6" ry="3.6"/>
            <path d="M3.4 7h7.2"/>
          </g>
        </svg>
      </li>
    </ul>
  </section>

  <section class="card card--back" aria-label="Business card back">
    <div class="back-brand">
      <span class="brand-mark"></span>
      <span>QUORVANE CAPITAL</span>
    </div>
    <p class="tagline">Diversified Crypto Investment Funds</p>
  </section>

</main>
</body>
</html>
```